The Birchwater Evenings - Concert Series Website Design

I've recently decided to launch a concert series in my living room and would love a website to use to promote the series. I'm looking for a simple Wix design that I could take over once it's complete. I'll provide the logo for which I'd like the website to utilize the color scheme.

Target Market(s)

Music lovers in Denver

Industry/Entity Type

Music

Coding

Coded - Design and coding required

Number of Pages Required

2 page

Font styles to use
Script

Requirements
Must have
• 2 pages - one for concert goers to see the schedule and rsvp, and one for artists about the booking process

```html
<!DOCTYPE html>
<html lang="en">
<head>
<meta charset="utf-8">
<title>The Birchwater Evenings</title>
<link href="https://fonts.googleapis.com/css2?family=Great+Vibes&family=Playfair+Display:ital@1&family=Poppins:wght@400;500;600;700&display=swap" rel="stylesheet">
<style>
:root{
  --cream:#fdf6ec;
  --plum:#4a1850;
  --plum-deep:#2a0d2f;
  --plum-mid:#6a2a6e;
  --amber:#f0a24a;
  --amber-deep:#e07a3a;
  --ink:#2b1a2c;
  --muted:#6d5c6e;
  --white:#ffffff;
  --line:#e6dccd;
}
*{box-sizing:border-box;margin:0;padding:0}
html,body{width:1200px;height:3220px;overflow:hidden}
body{font-family:'Poppins',sans-serif;background:var(--cream);color:var(--ink);position:relative}
.script{font-family:'Great Vibes',cursive;font-weight:400}
.btn{display:inline-block;font-size:12px;font-weight:600;letter-spacing:.08em;padding:14px 28px;border-radius:30px;text-transform:uppercase}
.btn-amber{background:linear-gradient(90deg,var(--amber),var(--amber-deep));color:var(--white)}
.btn-ghost{border:1.5px solid var(--white);color:var(--white)}
.btn-plum{background:var(--plum);color:var(--white)}
.btn-plum-ghost{border:1.5px solid var(--plum);color:var(--plum)}

/* hero */
.hero{position:absolute;left:0;top:0;width:1200px;height:580px}
.hero-photo{position:absolute;inset:0;background:radial-gradient(ellipse at 50% 40%,#8a5a38 0%,#4a2a20 45%,#1c0f12 100%)}
.hero-shade{position:absolute;inset:0;background:linear-gradient(180deg,rgba(20,8,14,.55),rgba(20,8,14,.35) 50%,rgba(20,8,14,.75))}
.nav{position:absolute;top:26px;left:90px;right:90px;display:flex;align-items:center;justify-content:space-between}
.brand{display:flex;align-items:center;gap:12px;color:var(--white);font-weight:600;font-size:20px;letter-spacing:.04em;text-transform:uppercase}
.brand-dot{width:34px;height:34px;border-radius:50%;background:var(--amber)}
.nav-links{display:flex;align-items:center;gap:32px;color:var(--white);font-size:13px;font-weight:500;letter-spacing:.06em}
.hero-text{position:absolute;top:275px;width:100%;text-align:center;color:var(--white)}
.hero-kicker{font-size:20px;font-weight:600;letter-spacing:.06em;text-transform:uppercase}
.hero-title{font-size:86px;line-height:1;margin:6px 0 8px}
.hero-sub{font-size:20px;margin-bottom:30px}
.hero-actions{display:flex;justify-content:center;gap:20px}

/* about */
.about{position:absolute;top:620px;left:0;width:1200px;height:500px}
.collage .ph{position:absolute;background:linear-gradient(160deg,#a86b3e,#5a2d3a 60%,#2a1324)}
.ph-a{left:140px;top:20px;width:240px;height:440px;border-radius:120px 120px 0 120px}
.ph-b{left:395px;top:20px;width:190px;height:190px;border-radius:50%;background:linear-gradient(160deg,#c0603a,#6a2050) !important}
.ph-c{left:395px;top:225px;width:190px;height:235px;border-radius:95px 95px 95px 0}
.about-copy{position:absolute;left:660px;top:50px;width:430px}
.eyebrow{font-size:13px;font-weight:600;letter-spacing:.12em;text-transform:uppercase;color:var(--plum)}
.about-title{font-size:58px;color:var(--plum);line-height:1.1}
.rule{width:60px;height:3px;background:var(--amber);margin:8px 0 18px}
.about-copy p{font-size:13px;line-height:1.75;color:var(--muted);margin-bottom:12px}
.about-copy p strong{color:var(--ink)}

/* features */
.features{position:absolute;top:1140px;left:140px;width:920px;display:flex;gap:26px}
.feature{flex:1;background:var(--white);border-radius:18px;box-shadow:0 8px 26px rgba(74,24,80,.12);height:210px;padding:28px 18px;text-align:center}
.feature svg{width:48px;height:48px;fill:var(--plum)}
.feature h3{font-size:32px;color:var(--plum);margin:8px 0 4px;line-height:1.1}
.feature p{font-size:12.5px;color:var(--muted);line-height:1.6}

/* music at dusk */
.dusk{position:absolute;top:1440px;left:0;width:1200px;height:480px}
.dusk-photo{position:absolute;inset:0;background:linear-gradient(100deg,#3a2018 0%,#7a4a2c 45%,#b07844 70%,#4a2a1e 100%)}
.dusk-card{position:absolute;left:140px;top:70px;width:340px;background:var(--cream);border-radius:18px;padding:30px 28px}
.dusk-card h2{font-size:48px;line-height:1.05;color:var(--plum)}
.dusk-card p{font-size:13px;line-height:1.7;color:var(--muted);margin:14px 0 22px}
.dusk-card .acts{display:flex;gap:12px}
.dusk-card .btn{padding:12px 18px;font-size:11px}

/* join */
.join{position:absolute;top:1990px;left:0;width:1200px;text-align:center}
.join .eyebrow{color:var(--amber-deep)}
.join h2{font-size:64px;color:var(--plum);line-height:1.1}
.join .rule{margin:4px auto 18px}
.join-lead{font-size:14px;line-height:1.7;color:var(--muted);width:560px;margin:0 auto 36px}
.form{width:620px;margin:0 auto;display:grid;grid-template-columns:1fr 1fr;gap:16px}
.field{background:var(--white);border:1px solid var(--line);border-radius:8px;height:50px;display:flex;align-items:center;gap:10px;padding:0 16px;font-size:13px;color:#a89aa8;text-align:left}
.field svg{width:16px;height:16px;fill:#b7a8b8}
.field.msg{grid-column:1/3;height:120px;align-items:flex-start;padding-top:16px}
.submit{grid-column:1/3;background:var(--plum);color:var(--white);border-radius:8px;height:52px;display:flex;align-items:center;justify-content:center;font-size:13px;font-weight:600;letter-spacing:.08em}

/* quote */
.quote{position:absolute;top:2560px;left:0;width:1200px;height:300px;background:linear-gradient(180deg,#6a2a6e,#3a1240);text-align:center;color:var(--white)}
.quote-mark{font-family:'Playfair Display',serif;font-size:120px;color:var(--amber);line-height:1;height:70px;margin-top:40px}
.quote p{font-family:'Playfair Display',serif;font-style:italic;font-size:30px;line-height:1.5;width:900px;margin:20px auto 0}

/* footer */
.footer{position:absolute;top:2860px;left:0;width:1200px;height:360px;background:var(--plum-deep);color:var(--white)}
.footer .brand{justify-content:center;margin-top:40px}
.social{display:flex;justify-content:center;gap:12px;margin-top:20px}
.social span{width:28px;height:28px;border-radius:50%;background:var(--amber)}
.contacts{display:flex;justify-content:space-between;width:1000px;margin:50px auto 0}
.contact{display:flex;align-items:center;gap:14px;font-size:13px;line-height:1.5}
.contact .ic{width:40px;height:40px;border-radius:50%;background:var(--white);display:flex;align-items:center;justify-content:center}
.contact svg{width:18px;height:18px;fill:var(--plum-deep)}
.copyright{position:absolute;bottom:0;left:0;width:100%;border-top:1px solid rgba(255,255,255,.15);text-align:center;font-size:12px;padding:22px 0;color:rgba(255,255,255,.75)}
</style>
</head>
<body>

<section class="hero">
  <div class="hero-photo" role="img" aria-label="Musicians performing for a seated audience in a warmly lit living room"></div>
  <div class="hero-shade"></div>
  <header class="nav">
    <div class="brand"><span class="brand-dot"></span>The Birchwater Evenings</div>
    <nav class="nav-links"><span>HOME</span><span>ABOUT US</span><span class="btn btn-amber" style="padding:10px 20px;font-size:11px">Contact Us</span></nav>
  </header>
  <div class="hero-text">
    <div class="hero-kicker">A Living Room Concert Series</div>
    <h1 class="hero-title script">The Birchwater Evenings</h1>
    <div class="hero-sub">Intimate Concerts in Denver's North End</div>
    <div class="hero-actions"><span class="btn btn-amber">Discover More</span><span class="btn btn-ghost">Stay Informed</span></div>
  </div>
</section>

<section class="about">
  <div class="collage">
    <div class="ph ph-a" role="img" aria-label="Guitarist and singer performing to guests in a living room"></div>
    <div class="ph ph-b" role="img" aria-label="Audience enjoying a concert under warm lights"></div>
    <div class="ph ph-c" role="img" aria-label="Singer performing with a microphone"></div>
  </div>
  <div class="about-copy">
    <div class="eyebrow">About Us</div>
    <h2 class="about-title script">The Birchwater Evenings</h2>
    <div class="rule"></div>
    <p><strong>I'm Delighted To Announce The Launch Of The Birchwater Evenings: Intimate Concerts In Denver's North End.</strong></p>
    <p>Inspired By The Quiet Radiance That Settles Over The Mountains At Dusk, The Birchwater Evenings Is A New Living Room Concert Series Devoted To Attentive Listening, Artistic Depth, And Shared Musical Experience. Hosted In My Home In Denver's North End Of Central Park, These Gatherings Will Bring Folks Together For Evenings Of Warmth, Nuance, And Connection.</p>
    <span class="btn btn-plum" style="margin-top:10px">Read More</span>
  </div>
</section>

<section class="features">
  <div class="feature">
    <svg viewBox="0 0 24 24"><circle cx="12" cy="7" r="3.2"/><circle cx="5" cy="9" r="2.4"/><circle cx="19" cy="9" r="2.4"/><path d="M6 20c0-3.6 2.7-6 6-6s6 2.4 6 6z"/><path d="M0 19c0-2.8 2-4.6 5-4.6 1 0 1.6.2 2.2.5C5.6 16.2 5 17.6 5 19z"/><path d="M24 19c0-2.8-2-4.6-5-4.6-1 0-1.6.2-2.2.5 1.6 1.3 2.2 2.7 2.2 4.1z"/></svg>
    <h3 class="script">21–40 Guests</h3>
    <p>Tiny Gatherings, Huge Intimacy. Every Note Shared.</p>
  </div>
  <div class="feature">
    <svg viewBox="0 0 24 24"><path d="M12 1.5c-4.4 0-8 3.4-8 7.8 0 5.6 8 13.2 8 13.2s8-7.6 8-13.2c0-4.4-3.6-7.8-8-7.8zm0 11a3.2 3.2 0 1 1 0-6.4 3.2 3.2 0 0 1 0 6.4z"/></svg>
    <h3 class="script">North End Denver</h3>
    <p>Hosted In My Home In Central Park — Cozy &amp; Welcoming</p>
  </div>
  <div class="feature">
    <svg viewBox="0 0 24 24"><path d="M9 3l12-2v14.5a3 3 0 1 1-2-2.8V5.3l-8 1.4v10.8A3 3 0 1 1 9 14.7z"/></svg>
    <h3 class="script">Attentive Listening</h3>
    <p>Concerts Designed For Depth, Not Distraction.</p>
  </div>
  <div class="feature">
    <svg viewBox="0 0 24 24"><path d="M7 1h2v3h6V1h2v3h4v19H3V4h4zM5 9v12h14V9zm2 2h3v3H7zm5 0h3v3h-3zm-5 5h3v3H7zm5 0h3v3h-3z"/></svg>
    <h3 class="script">Inaugural Date</h3>
    <p>Artist Lineup &amp; First Concert Announced Soon</p>
  </div>
</section>

<section class="dusk">
  <div class="dusk-photo" role="img" aria-label="Musicians with guitar and voices performing for guests on sofas in a lamplit room"></div>
  <div class="dusk-card">
    <h2 class="script">The Birchwater Evenings: Music At Dusk</h2>
    <p>Inspired By The Soft Mountain Glow At Twilight, These Intimate Home Concerts Invite Attentive Listening, Nuance, And Human Connection In Denver's North End.</p>
    <div class="acts"><span class="btn btn-plum">Discover More</span><span class="btn btn-plum-ghost">Stay Informed</span></div>
  </div>
</section>

<section class="join">
  <div class="eyebrow">Stay Connected</div>
  <h2 class="script">Join Us</h2>
  <div class="rule"></div>
  <p class="join-lead">Our Inaugural Concert Date And Artist Lineup Will Be Announced Soon. Seating Will Be Limited, And Reservations Will Be Required.</p>
  <div class="form">
    <div class="field"><svg viewBox="0 0 24 24"><circle cx="12" cy="8" r="4"/><path d="M4 21c0-4.4 3.6-7 8-7s8 2.6 8 7z"/></svg>First Name</div>
    <div class="field"><svg viewBox="0 0 24 24"><circle cx="12" cy="8" r="4"/><path d="M4 21c0-4.4 3.6-7 8-7s8 2.6 8 7z"/></svg>Last Name</div>
    <div class="field"><svg viewBox="0 0 24 24"><path d="M2 5h20v14H2zm2 2v.5l8 5 8-5V7z"/></svg>Your Email</div>
    <div class="field"><svg viewBox="0 0 24 24"><path d="M6.6 10.8a15 15 0 0 0 6.6 6.6l2.2-2.2c.3-.3.7-.4 1-.2 1.1.4 2.3.6 3.6.6.6 0 1 .4 1 1V20c0 .6-.4 1-1 1A17 17 0 0 1 3 4c0-.6.4-1 1-1h3.5c.6 0 1 .4 1 1 0 1.3.2 2.5.6 3.6.1.3 0 .7-.2 1z"/></svg>Phone</div>
    <div class="field msg"><svg viewBox="0 0 24 24"><path d="M2 3h20v14H6l-4 4z"/></svg>Your Message</div>
    <div class="submit">SUBMIT NOW</div>
  </div>
</section>

<section class="quote">
  <div class="quote-mark">&ldquo;</div>
  <p>Extraordinary music does not require a grand hall. It requires space, intention, and a community willing to listen.</p>
</section>

<footer class="footer">
  <div class="brand"><span class="brand-dot"></span>The Birchwater Evenings</div>
  <div class="social"><span></span><span></span><span></span></div>
  <div class="contacts">
    <div class="contact"><span class="ic"><svg viewBox="0 0 24 24"><path d="M12 1.5c-4.4 0-8 3.4-8 7.8 0 5.6 8 13.2 8 13.2s8-7.6 8-13.2c0-4.4-3.6-7.8-8-7.8zm0 11a3.2 3.2 0 1 1 0-6.4 3.2 3.2 0 0 1 0 6.4z"/></svg></span><span>Intimate Concerts In<br>Denver's North End</span></div>
    <div class="contact"><span class="ic"><svg viewBox="0 0 24 24"><path d="M6.6 10.8a15 15 0 0 0 6.6 6.6l2.2-2.2c.3-.3.7-.4 1-.2 1.1.4 2.3.6 3.6.6.6 0 1 .4 1 1V20c0 .6-.4 1-1 1A17 17 0 0 1 3 4c0-.6.4-1 1-1h3.5c.6 0 1 .4 1 1 0 1.3.2 2.5.6 3.6.1.3 0 .7-.2 1z"/></svg></span><span>Phone<br>(555) 014-2290</span></div>
    <div class="contact"><span class="ic"><svg viewBox="0 0 24 24"><path d="M2 5h20v14H2zm2 2v.5l8 5 8-5V7z"/></svg></span><span>Email<br>hello@birchwaterevenings.com</span></div>
  </div>
  <div class="copyright">© 2026 The Birchwater Evenings. All Rights Reserved.</div>
</footer>

</body>
</html>
```